Wedding invitation - including print files

Details
45 invitations and envelopes required

Our names: Corin and Marisol

Wedding information
Venue
At the Pennington residence, 2847 Thornbury-Waipiro road, Clevedon, Auckland for both the ceremony and reception.

Date
Saturday 19th April 2025 (Easter weekend)

Timing
Ceremony is at 3pm

Transport
A bus will pick up at 1.30pm from Linden Crest Hotel
A bus will go back to town to at 11pm and 12.15am to Linden Crest Hotel with a stop through Clevedon for those staying closer to the venue.

Accomodation
A lot of roomshares and hotels in clevedon if you wish to stay closer

Gifts
gifts aren’t necessary but a wishing well for a piece of art we will remember the day by.

Day After
We will be having some platters from 1pm on Sunday at (I will confirm this to you tomorrow sorry we are choosing between two places)

RSVP
By the 12th October 2024 to Corin 0279416652 corin@brantleygroup.co or Marisol 0278815927 marisol@quellastudio.co.nz

Here are concept ideas for the invitations and the aspects we like about them.
Three sided is practical to fit information

Font styles to use
Decorative

Colors

Designer to choose only greyscale colors for use in the design.

Requirements
Nice to have
• refer attachments and description
Should not have
• cant look cheap or tacky

```html
<!DOCTYPE html>
<html lang="en">
<head>
<meta charset="utf-8">
<title>Corin &amp; Marisol – Wedding Invitation</title>
<link rel="stylesheet" href="https://fonts.googleapis.com/css2?family=Playfair+Display:wght@400;500&display=swap">
<style>
  :root {
    --backdrop: #ebebeb;
    --panel-info: #f1f1f1;
    --panel-main: #e4e4e4;
    --panel-cover: #cbcbcb;
    --ink: #1e1e1e;
    --ink-soft: #3a3a3a;
    --art-tone: #c4c4c4;
    --art-tone-light: #dadada;
  }
  * { box-sizing: border-box; margin: 0; padding: 0; }
  html, body {
    width: 1200px; height: 900px; overflow: hidden;
    background: var(--backdrop);
  }
  .invitation {
    position: absolute; left: 50px; top: 40px;
    width: 1101px; height: 820px;
    display: flex;
    box-shadow: 0 6px 24px rgba(0,0,0,0.12);
    font-family: "Playfair Display", Georgia, serif;
    color: var(--ink);
  }
  .panel { position: relative; height: 100%; }

  /* Left information flap */
  .panel-info { width: 257px; background: var(--panel-info); }
  .info-section {
    position: absolute; left: 0; width: 100%;
    padding: 0 24px; text-align: center;
  }
  .info-heading {
    font-size: 15px; font-weight: 400; letter-spacing: 0.14em;
    margin-bottom: 24px;
  }
  .info-text {
    font-size: 13px; line-height: 17.5px; color: var(--ink-soft);
  }
  .info-transport { top: 138px; }
  .info-accommodation { top: 355px; }
  .info-gifts { top: 476px; }
  .info-day-after { top: 623px; }

  /* Centre panel */
  .panel-main { width: 571px; background: var(--panel-main); text-align: center; }
  .venue-art {
    position: absolute; left: 59px; top: 47px; width: 450px; height: 332px;
    border-radius: 48% 48% 40% 40%;
    background: radial-gradient(ellipse at 50% 45%, var(--art-tone) 0%, var(--art-tone-light) 70%, var(--panel-main) 100%);
  }
  .couple-names {
    position: absolute; top: 382px; left: 0; width: 100%;
    font-size: 39px; font-weight: 400; letter-spacing: 0.08em;
  }
  .invite-line {
    position: absolute; top: 452px; left: 0; width: 100%;
    font-size: 13px; line-height: 28px; letter-spacing: 0.1em;
    text-transform: uppercase;
  }
  .wedding-date {
    position: absolute; top: 618px; left: 0; width: 100%;
    font-size: 28px; font-weight: 400;
  }
  .wedding-date sup { font-size: 14px; }
  .wedding-note {
    position: absolute; top: 656px; left: 0; width: 100%;
    font-size: 19px;
  }
  .rsvp {
    position: absolute; top: 713px; left: 0; width: 100%;
    font-size: 11px; line-height: 14px; letter-spacing: 0.05em;
  }

  /* Right cover flap */
  .panel-cover { width: 273px; background: var(--panel-cover); }
  .rose-art {
    position: absolute; left: 103px; top: 293px; width: 68px; height: 183px;
    background: linear-gradient(180deg, #a9a9a9 0%, #bdbdbd 100%);
    border-radius: 34px 34px 6px 6px;
  }
</style>
</head>
<body>
  <main class="invitation">
    <section class="panel panel-info">
      <div class="info-section info-transport">
        <h2 class="info-heading">TRANSPORT</h2>
        <p class="info-text">A bus will pick up at 1.30pm<br>from Linden Crest Hotel<br>A bus will go back to town to<br>at 11pm and 12.15am to Linden<br>Crest Hotel with a stop<br>through Clevedon for those<br>staying closer to the venue.</p>
      </div>
      <div class="info-section info-accommodation">
        <h2 class="info-heading">ACCOMODATION</h2>
        <p class="info-text">A lot of roomshares and hotels in<br>clevedon if you wish to stay closer</p>
      </div>
      <div class="info-section info-gifts">
        <h2 class="info-heading">GIFTS</h2>
        <p class="info-text">Gifts aren’t necessary but a<br>wishing well for a piece of art we<br>will remember the day by.</p>
      </div>
      <div class="info-section info-day-after">
        <h2 class="info-heading">DAY AFTER</h2>
        <p class="info-text">We will be having some platters<br>from 1pm on Sunday at<br>(I will confirm this to you<br>tomorrow sorry we are choosing<br>between two places)</p>
      </div>
    </section>

    <section class="panel panel-main">
      <div class="venue-art" role="img" aria-label="Pen sketch of the country homestead venue with trees and a curving driveway"></div>
      <h1 class="couple-names">CORIN &amp; MARISOL</h1>
      <p class="invite-line">Invite you to the ceremony and celebration of<br>their marriage 3pm at the Pennington residence,<br>2847 Thornbury-Waipiro road, Clevedon, Auckland<br>for both the ceremony and reception.</p>
      <p class="wedding-date">Saturday 19<sup>th</sup> April 2025</p>
      <p class="wedding-note">(Easter weekend)</p>
      <p class="rsvp">RSVP<br>By the 12th October 2024 to Corin 0279416652 corin@brantleygroup.co<br>or Marisol 0278815927 marisol@quellastudio.co.nz</p>
    </section>

    <section class="panel panel-cover">
      <div class="rose-art" role="img" aria-label="Fine line drawing of a single rose on a long stem"></div>
    </section>
  </main>
</body>
</html>
```